Brivane - Business Cards for a new venture

create business card for a startup classified business dealing in construction materials, the cards need to have a professional look but modern, more serious than playful, one of the samples must include the official font (attached), please explore using the official colors in the company's logo

Target Market(s)

Energy sector

Contact Information for Business Card

Font styles to use
Other font styles liked:
• suissnord

Requirements
Must have
• corporate colors (in logo attached)
Nice to have
• Official font (in one of the samples) font is : suissnord
Should not have
• Cartoonish look

```html
<!DOCTYPE html>
<html lang="en">
<head>
<meta charset="UTF-8">
<title>Brivane – Business Cards</title>
<link rel="stylesheet" href="https://fonts.googleapis.com/css2?family=Michroma&family=Montserrat:wght@400;500&display=swap">
<style>
  :root {
    --backdrop: #262626;
    --card: #121212;
    --blue: #3d9be4;
    --icon-blue: #1e9ee8;
    --grey: #a9a9a9;
    --text: #e6e6e6;
  }
  * { box-sizing: border-box; margin: 0; padding: 0; }
  html, body {
    width: 1200px; height: 900px; overflow: hidden;
    background: var(--backdrop);
  }
  .canvas {
    position: relative; width: 1200px; height: 900px;
    display: flex; flex-direction: column; align-items: center; justify-content: center; gap: 30px;
  }
  .card {
    position: relative; width: 720px; height: 411px;
    background: var(--card);
    box-shadow: 0 6px 18px rgba(0,0,0,.45);
    font-family: "Montserrat", sans-serif; color: var(--text);
  }
  .wordmark {
    font-family: "Montserrat", sans-serif; font-weight: 500;
    color: var(--grey); letter-spacing: 6px; text-transform: uppercase;
    display: flex; align-items: center; gap: 12px;
  }
  .wordmark .mark-dot {
    width: 14px; height: 14px; border-radius: 50%; background: var(--blue);
  }

  /* back face */
  .card-back .wordmark {
    position: absolute; top: 112px; left: 0; right: 0; justify-content: center;
    font-size: 34px;
  }
  .card-back .rule {
    position: absolute; top: 184px; left: 242px; width: 236px; height: 4px; background: var(--blue);
  }
  .card-back .phone {
    position: absolute; top: 262px; left: 0; right: 0;
    display: flex; justify-content: center; align-items: center; gap: 12px;
    font-size: 19px; letter-spacing: 2px;
  }

  /* front face */
  .card-front .wordmark {
    position: absolute; top: 98px; left: 68px; font-size: 30px;
  }
  .identity {
    position: absolute; top: 40px; right: 58px; text-align: right;
  }
  .identity .person {
    font-family: "Michroma", sans-serif; color: var(--blue);
    font-size: 22px; letter-spacing: 1px; text-transform: uppercase;
  }
  .identity .role {
    font-family: "Michroma", sans-serif; color: var(--text);
    font-size: 11px; letter-spacing: 1px; text-transform: uppercase; margin-top: 6px;
    padding-bottom: 6px; border-bottom: 2px solid var(--blue);
    display: inline-block; width: 176px; text-align: left; padding-left: 2px;
  }
  .band {
    position: absolute; top: 256px; left: 0; width: 100%; height: 6px; background: var(--blue);
  }
  .contacts {
    position: absolute; top: 292px; left: 52px; right: 52px;
    display: grid; grid-template-columns: 1fr 200px; row-gap: 18px;
    font-size: 17px; letter-spacing: .5px;
  }
  .contact { display: flex; align-items: center; gap: 14px; }
  .contact svg { width: 18px; height: 18px; flex: none; }
</style>
</head>
<body>
<main class="canvas">

  <section class="card card-back">
    <div class="wordmark"><span class="mark-dot"></span>Brivane</div>
    <div class="rule"></div>
    <div class="phone">
      <svg width="18" height="18" viewBox="0 0 24 24" aria-hidden="true"><path fill="#1e9ee8" d="M6.6 10.8a15.1 15.1 0 0 0 6.6 6.6l2.2-2.2a1 1 0 0 1 1-.25 11.4 11.4 0 0 0 3.6.57 1 1 0 0 1 1 1V20a1 1 0 0 1-1 1A17 17 0 0 1 3 4a1 1 0 0 1 1-1h3.5a1 1 0 0 1 1 1c0 1.25.2 2.45.57 3.6a1 1 0 0 1-.25 1z"/></svg>
      <span>0455 812 306</span>
    </div>
  </section>

  <section class="card card-front">
    <div class="wordmark"><span class="mark-dot"></span>Brivane</div>
    <div class="identity">
      <div class="person">Daren Holt</div>
      <div class="role">Graphic Designer</div>
    </div>
    <div class="band"></div>
    <div class="contacts">
      <div class="contact">
        <svg viewBox="0 0 24 24" aria-hidden="true"><path fill="#1e9ee8" d="M12 2a7 7 0 0 0-7 7c0 5.2 7 13 7 13s7-7.8 7-13a7 7 0 0 0-7-7zm0 9.5A2.5 2.5 0 1 1 12 6.5a2.5 2.5 0 0 1 0 5z"/></svg>
        <span>48, Harbor Lane&nbsp; Corvale, Ohio, USA</span>
      </div>
      <div class="contact">
        <svg viewBox="0 0 24 24" aria-hidden="true"><path fill="#1e9ee8" d="M6.6 10.8a15.1 15.1 0 0 0 6.6 6.6l2.2-2.2a1 1 0 0 1 1-.25 11.4 11.4 0 0 0 3.6.57 1 1 0 0 1 1 1V20a1 1 0 0 1-1 1A17 17 0 0 1 3 4a1 1 0 0 1 1-1h3.5a1 1 0 0 1 1 1c0 1.25.2 2.45.57 3.6a1 1 0 0 1-.25 1z"/></svg>
        <span>0455 812 306</span>
      </div>
      <div class="contact">
        <svg viewBox="0 0 24 24" aria-hidden="true"><rect x="2.5" y="5" width="19" height="14" fill="none" stroke="#1e9ee8" stroke-width="2"/><path d="M3 6l9 7 9-7M3 18l7-6M21 18l-7-6" fill="none" stroke="#1e9ee8" stroke-width="1.6"/></svg>
        <span>Hello@Brivanemail.Com</span>
      </div>
      <div class="contact">
        <svg viewBox="0 0 24 24" aria-hidden="true"><rect x="7" y="2" width="10" height="20" rx="1.5" fill="none" stroke="#1e9ee8" stroke-width="2"/><rect x="9" y="5" width="6" height="5" fill="#1e9ee8"/><path d="M9 13h2v2H9zm4 0h2v2h-2zm-4 3h2v2H9zm4 0h2v2h-2z" fill="#1e9ee8"/></svg>
        <span>0455 812 306</span>
      </div>
    </div>
  </section>

</main>
</body>
</html>
```